Book cover for modern/pop-culture-oriented poetry collection

We need a simple, streamlined book-cover design (that'll ultimately be 1600 x 2500 pixels; 300 dpi) for a book of poems. We would like to see three elements on the cover: (1) the title in all caps (GLASSHOURS); (2) the author name in all caps (MIRA VENTO); (3) the main image (attached, slugged "glasshours image"). Image and text should be centered on the cover.

Target Market(s)

Readers of contemporary poetry

Font styles to use
Sans Serif

Requirements
Must have
• Book title, author name, attached photo
Nice to have
• Also attached is the cover of a book (HARBOUR) that is in the style/spirit of what we're looking for.

```html
<!DOCTYPE html>
<html lang="en">
<head>
<meta charset="utf-8">
<title>Glasshours — Mira Vento</title>
<link rel="stylesheet" href="https://fonts.googleapis.com/css2?family=Josefin+Sans:wght@300&display=swap">
<style>
  :root {
    --page: #ffffff;
    --wood-light: #b8652a;
    --wood-mid: #8e4a1c;
    --wood-dark: #5a2e12;
    --bezel: #efe3b8;
    --screen-dark: #1a1512;
    --type: #ffffff;
  }
  html, body {
    margin: 0;
    padding: 0;
    width: 1200px;
    height: 1200px;
    overflow: hidden;
    background: var(--page);
  }
  .canvas {
    position: relative;
    width: 1200px;
    height: 1200px;
    background: var(--page);
  }
  .book-cover {
    position: absolute;
    left: 266px;
    top: 44px;
    width: 667px;
    height: 1111px;
    overflow: hidden;
  }
  .cover-image {
    position: absolute;
    inset: 0;
    background:
      linear-gradient(170deg,
        var(--wood-mid) 0%,
        var(--wood-light) 4%,
        var(--bezel) 9%,
        var(--screen-dark) 15%,
        var(--screen-dark) 36%,
        var(--bezel) 44%,
        var(--wood-light) 50%,
        var(--wood-mid) 54%,
        var(--bezel) 60%,
        var(--screen-dark) 67%,
        var(--screen-dark) 87%,
        var(--bezel) 93%,
        var(--wood-dark) 100%);
  }
  .cover-text {
    position: absolute;
    left: 50%;
    transform: translate(-50%, -50%);
    margin: 0;
    font-family: "Josefin Sans", sans-serif;
    font-weight: 300;
    font-size: 50px;
    color: var(--type);
    white-space: nowrap;
    letter-spacing: 0;
    line-height: 1;
  }
  .book-title {
    top: 248px;
  }
  .book-author {
    top: 834px;
  }
</style>
</head>
<body>
  <main class="canvas">
    <section class="book-cover">
      <div class="cover-image" role="img" aria-label="glasshours image: two stacked vintage wood-cabinet television sets with cream bezels and dark blank screens, set at a slight angle in front of shelves of tapes"></div>
      <h1 class="cover-text book-title">GLASSHOURS</h1>
      <p class="cover-text book-author">MIRA VENTO</p>
    </section>
  </main>
</body>
</html>
```